Vesit cards for web development company

We need a business card design for our company. The company develops online platforms and conducts marketing consulting. Company logo. The cards must fit in with us (a junior start UP), but they must also be professional enough to impress with investors like banks. We wish you a combination of classic and modern design

Target Market(s)

Business partners and IT and marketing customers

Industry/Entity Type

It Company

Contact Information for Business Card

Folgende Information müssen Drauf.
Name, Position, Telefon Nr., Mobile Nr., E-Mail adresse, Optional sind noch Webadresse und HRB Nummer

Colors

Designer to choose colors to be used in the design.

Requirements
Must have
• The cards have to fit into the logo later and have to be dynamic and serious at the same time

```html
<!DOCTYPE html>
<html lang="en">
<head>
<meta charset="UTF-8">
<title>Norvale Development – Business Card</title>
<link href="https://fonts.googleapis.com/css2?family=Open+Sans:wght@400;600;700;800&display=swap" rel="stylesheet">
<style>
  :root {
    --page-bg: #e6e8eb;
    --brand-blue: #1f75bf;
    --swoosh-grey: #9da1a6;
    --silver-light: #d9dadc;
    --silver-mid: #b3b5b8;
    --silver-dark: #8f9195;
    --paper: #ffffff;
    --ink: #4a4d52;
    --white: #ffffff;
  }
  * { margin: 0; padding: 0; box-sizing: border-box; }
  html, body {
    width: 1200px; height: 900px; overflow: hidden;
    background: var(--page-bg);
    font-family: "Open Sans", Arial, sans-serif;
  }
  .canvas { position: relative; width: 1200px; height: 900px; }
  .card {
    position: absolute; left: 285px;
    width: 630px; height: 360px;
    overflow: hidden;
    box-shadow: 0 10px 28px rgba(0,0,0,0.18);
  }
  .card-front { top: 60px;
    background: linear-gradient(115deg, var(--silver-light) 0%, var(--silver-mid) 45%, var(--silver-dark) 100%);
  }
  .card-back { top: 480px; background: var(--paper); }

  /* front */
  .front-wordmark {
    position: absolute; left: 0; right: 0; top: 108px;
    text-align: center; color: var(--white);
    font-weight: 800; font-size: 46px; line-height: 1.05; letter-spacing: 1px;
    text-transform: uppercase;
  }
  .front-url {
    position: absolute; left: 0; right: 0; top: 276px;
    text-align: center; color: var(--white);
    font-size: 14px; letter-spacing: 6px;
  }

  /* back */
  .back-art { position: absolute; inset: 0; width: 100%; height: 100%; }
  .holder {
    position: absolute; right: 40px; top: 34px;
    text-align: right; color: var(--white);
  }
  .holder-name { font-weight: 700; font-size: 15px; text-transform: uppercase; }
  .holder-role { font-size: 14px; text-transform: uppercase; margin-top: 2px; }
  .back-wordmark {
    position: absolute; left: 60px; top: 200px;
    color: var(--brand-blue);
    font-weight: 800; font-size: 28px; line-height: 1.05;
    text-transform: uppercase;
  }
  .contact-list {
    position: absolute; left: 62px; top: 272px;
    list-style: none; color: var(--ink); font-size: 14px; line-height: 19px;
  }
  .contact-list li { display: flex; align-items: center; gap: 9px; }
  .contact-list svg { width: 12px; height: 12px; fill: var(--brand-blue); flex: none; }
</style>
</head>
<body>
<main class="canvas">

  <section class="card card-front">
    <div class="front-wordmark">Norvale<br>Development</div>
    <div class="front-url">www.norvaledevelopment.com</div>
  </section>

  <section class="card card-back">
    <svg class="back-art" viewBox="0 0 630 360" preserveAspectRatio="none">
      <rect width="630" height="360" fill="var(--brand-blue)"/>
      <path d="M0,178 C60,124 260,94 630,88 L630,106 C260,112 62,146 0,196 Z" fill="var(--swoosh-grey)"/>
      <path d="M0,200 C62,150 260,116 630,110 L630,360 L0,360 Z" fill="var(--paper)"/>
    </svg>

    <div class="holder">
      <div class="holder-name">Mark Elling</div>
      <div class="holder-role">CEO/Founder</div>
    </div>

    <div class="back-wordmark">Norvale<br>Development</div>

    <ul class="contact-list">
      <li><svg viewBox="0 0 24 24"><path d="M6.6 10.8a15 15 0 0 0 6.6 6.6l2.2-2.2a1 1 0 0 1 1-.25 11.4 11.4 0 0 0 3.6.57 1 1 0 0 1 1 1V20a1 1 0 0 1-1 1A17 17 0 0 1 3 4a1 1 0 0 1 1-1h3.5a1 1 0 0 1 1 1c0 1.25.2 2.45.57 3.6a1 1 0 0 1-.25 1z"/></svg>555 210 4871</li>
      <li><svg viewBox="0 0 24 24"><path d="M7 1h10a2 2 0 0 1 2 2v18a2 2 0 0 1-2 2H7a2 2 0 0 1-2-2V3a2 2 0 0 1 2-2zm0 3v14h10V4z"/></svg>555 382 6140</li>
      <li><svg viewBox="0 0 24 24"><path d="M2 5h20v14H2zm2 2v.5l8 5 8-5V7z"/></svg>mark@norvaledev.com</li>
      <li><svg viewBox="0 0 24 24"><circle cx="12" cy="12" r="10"/></svg>www.norvaledev.com</li>
    </ul>
  </section>

</main>
</body>
</html>
```